Personal sales brochure for client marketing

I am looking for a brochure in the style of a sales menu to sit in front of clients with. I want 5 different colored columns where clients will choose the right package for them.
Eg.
Package 1 called Book-keeping is a basic package
Package 2 called Insight includes the above but also extra services
Package 3 called Compliance an add on for the above packages
Package 4 Called Professional another add on to the above services
Package 5 called payroll another add on to the above.

I want to sit in front of my clients and discuss the services we provide and allow them to choose from this list and tick the boxes of what they would like. I attach a simple spread sheet as well for guideline.

Target Market(s)

business owners requiring accounting support and advice

Industry/Entity Type

Accounting

Font styles to use
Serif
Sans Serif

Requirements
Must have
• Simple, clear, concise with clear product descriptions in colored boxes that highlight clearly the different options. Must have Logo and contact details. This document need to be our key sales and marketing tool so will need to introduce the business clearly and in a professional manner.
• enquiries@brantwellpartners.gg
• 01481 439216
Nice to have
• The design needs to be printable on A1 A3 A4 A5
Should not have
• Pictures and patterns

```html
<!DOCTYPE html>
<html lang="en">
<head>
<meta charset="utf-8">
<title>Brantwell Partners – Service Packages</title>
<link rel="stylesheet" href="https://fonts.googleapis.com/css2?family=Roboto:wght@300;400;500&display=swap">
<style>
  :root {
    --bookkeeping: #56b847;
    --insight: #2a9d8f;
    --compliance: #3b7fc4;
    --professional: #e9822b;
    --payroll: #7b5ea7;
    --dark: #2b2b2b;
    --cell: #e6e6e7;
    --ink: #3a3a3a;
    --paper: #ffffff;
    --pencil-orange: #f08a2c;
    --pencil-wood: #f3d3a8;
  }
  html, body {
    margin: 0;
    padding: 0;
    overflow: hidden;
    background: var(--paper);
  }
  .sheet {
    position: relative;
    width: 1200px;
    height: 848px;
    overflow: hidden;
    background: var(--paper);
    font-family: "Roboto", "Helvetica Neue", Arial, sans-serif;
    color: var(--ink);
  }
  .hero-photo {
    position: absolute;
    left: 510px;
    top: 0;
    width: 662px;
    height: 196px;
    background: linear-gradient(180deg, var(--pencil-orange) 0%, var(--pencil-wood) 45%, #ffffff 100%);
  }
  .brand {
    position: absolute;
    left: 72px;
    top: 72px;
  }
  .brand-name {
    margin: 0;
    font-size: 29px;
    font-weight: 300;
    letter-spacing: 1px;
    color: var(--dark);
    line-height: 1;
    text-transform: uppercase;
  }
  .brand-tagline {
    margin: 9px 0 0;
    font-size: 10.5px;
    font-weight: 400;
    letter-spacing: 2.4px;
    color: var(--dark);
  }
  .headline {
    position: absolute;
    left: 71px;
    top: 150px;
    margin: 0;
    font-size: 27px;
    font-weight: 300;
    color: var(--dark);
  }
  .headline .accent { color: var(--bookkeeping); }

  .options-table {
    position: absolute;
    left: 71px;
    top: 210px;
    display: grid;
    grid-template-columns: 177px repeat(5, 174px);
    grid-template-rows: 88px repeat(15, 30px);
    column-gap: 3px;
    row-gap: 3px;
  }
  .description-label {
    grid-column: 1; grid-row: 1;
    align-self: end;
    padding: 0 0 22px 20px;
    font-size: 17px;
    font-weight: 300;
    color: var(--bookkeeping);
  }
  .option-head {
    grid-row: 1;
    align-self: end;
    height: 76px;
    color: #fff;
    font-size: 22px;
    font-weight: 300;
    display: flex;
    align-items: center;
    justify-content: center;
  }
  .option-head.featured { height: 88px; }
  .head-bookkeeping  { grid-column: 2; background: var(--bookkeeping); }
  .head-insight      { grid-column: 3; background: var(--insight); }
  .head-compliance   { grid-column: 4; background: var(--compliance); }
  .head-professional { grid-column: 5; background: var(--professional); }
  .head-payroll      { grid-column: 6; background: var(--payroll); }

  .service {
    grid-column: 1;
    width: 167px;
    height: 30px;
    background: var(--dark);
    color: #fff;
    font-size: 11.5px;
    font-weight: 300;
    display: flex;
    align-items: center;
    padding-left: 9px;
    box-sizing: border-box;
    white-space: nowrap;
    clip-path: polygon(0 0, calc(100% - 17px) 0, 100% 50%, calc(100% - 17px) 100%, 0 100%);
  }
  .service.wide {
    grid-column: 1 / span 5;
    width: 876px;
    justify-content: flex-end;
    padding-right: 32px;
  }
  .cell {
    height: 30px;
    background: var(--cell);
    display: flex;
    align-items: center;
    justify-content: center;
  }
  .c2 { grid-column: 2; color: var(--bookkeeping); }
  .c3 { grid-column: 3; color: var(--insight); }
  .c4 { grid-column: 4; color: var(--compliance); }
  .c5 { grid-column: 5; color: var(--professional); }
  .c6 { grid-column: 6; color: var(--payroll); }
  .tick { width: 19px; height: 19px; }
  .dot {
    width: 18px; height: 18px;
    border-radius: 50%;
    background: var(--dark);
  }
  .contact {
    position: absolute;
    left: 71px;
    right: 67px;
    top: 808px;
    display: flex;
    justify-content: space-between;
    font-size: 13px;
    font-weight: 400;
    color: var(--dark);
  }
  .contact .label { color: var(--bookkeeping); margin-right: 6px; }
</style>
</head>
<body>
<main class="sheet">
  <div class="hero-photo" role="img" aria-label="Row of sharpened orange pencils with a single blue pencil standing out"></div>

  <header class="brand">
    <p class="brand-name">Brantwell Partners</p>
    <p class="brand-tagline">ACCOUNTING &amp; BUSINESS SOLUTIONS</p>
  </header>

  <h1 class="headline"><span class="accent">Sharpening our pencils</span> together</h1>

  <svg width="0" height="0" style="position:absolute" aria-hidden="true">
    <symbol id="tick" viewBox="0 0 24 24">
      <circle cx="12" cy="12" r="10" fill="none" stroke="currentColor" stroke-width="2.4"/>
      <path d="M7.3 12.3l3.2 3.2 6.2-6.4" fill="none" stroke="currentColor" stroke-width="2.6" stroke-linecap="round" stroke-linejoin="round"/>
    </symbol>
  </svg>

  <section class="options-table">
    <div class="description-label">Description</div>
    <div class="option-head head-bookkeeping">Book-keeping</div>
    <div class="option-head head-insight">Insight</div>
    <div class="option-head head-compliance">Compliance</div>
    <div class="option-head head-professional">Professional</div>
    <div class="option-head head-payroll featured">Payroll</div>

    <div class="service" style="grid-row:2">Bank reconciliations</div>
    <div class="service" style="grid-row:3">Sales ledger</div>
    <div class="service" style="grid-row:4">Purchase ledger</div>
    <div class="service" style="grid-row:5">Cloud software setup</div>
    <div class="service" style="grid-row:6">Management accounts</div>
    <div class="service" style="grid-row:7">KPI dashboard</div>
    <div class="service" style="grid-row:8">Quarterly review</div>
    <div class="service" style="grid-row:9">Annual accounts</div>
    <div class="service" style="grid-row:10">Income tax returns</div>
    <div class="service" style="grid-row:11">Company secretarial</div>
    <div class="service" style="grid-row:12">Business planning</div>
    <div class="service" style="grid-row:13">Cash flow forecasting</div>
    <div class="service" style="grid-row:14">Dedicated partner</div>
    <div class="service wide" style="grid-row:15">Monthly payroll processing</div>
    <div class="service wide" style="grid-row:16">Social security &amp; pension returns</div>

    <div class="cell c2" style="grid-row:2"><span class="dot"></span></div>
    <div class="cell c2" style="grid-row:3"><span class="dot"></span></div>
    <div class="cell c2" style="grid-row:4"><span class="dot"></span></div>
    <div class="cell c2" style="grid-row:5"><span class="dot"></span></div>

    <div class="cell c3" style="grid-row:2"><svg class="tick"><use href="#tick"/></svg></div>
    <div class="cell c3" style="grid-row:3"><svg class="tick"><use href="#tick"/></svg></div>
    <div class="cell c3" style="grid-row:4"><svg class="tick"><use href="#tick"/></svg></div>
    <div class="cell c3" style="grid-row:5"><svg class="tick"><use href="#tick"/></svg></div>
    <div class="cell c3" style="grid-row:6"><svg class="tick"><use href="#tick"/></svg></div>
    <div class="cell c3" style="grid-row:7"><svg class="tick"><use href="#tick"/></svg></div>
    <div class="cell c3" style="grid-row:8"><svg class="tick"><use href="#tick"/></svg></div>

    <div class="cell c4" style="grid-row:2"><svg class="tick"><use href="#tick"/></svg></div>
    <div class="cell c4" style="grid-row:3"><svg class="tick"><use href="#tick"/></svg></div>
    <div class="cell c4" style="grid-row:4"><svg class="tick"><use href="#tick"/></svg></div>
    <div class="cell c4" style="grid-row:5"><svg class="tick"><use href="#tick"/></svg></div>
    <div class="cell c4" style="grid-row:6"><svg class="tick"><use href="#tick"/></svg></div>
    <div class="cell c4" style="grid-row:7"><svg class="tick"><use href="#tick"/></svg></div>
    <div class="cell c4" style="grid-row:8"><svg class="tick"><use href="#tick"/></svg></div>
    <div class="cell c4" style="grid-row:9"><svg class="tick"><use href="#tick"/></svg></div>
    <div class="cell c4" style="grid-row:10"><svg class="tick"><use href="#tick"/></svg></div>
    <div class="cell c4" style="grid-row:11"><svg class="tick"><use href="#tick"/></svg></div>

    <div class="cell c5" style="grid-row:2"><svg class="tick"><use href="#tick"/></svg></div>
    <div class="cell c5" style="grid-row:3"><svg class="tick"><use href="#tick"/></svg></div>
    <div class="cell c5" style="grid-row:4"><svg class="tick"><use href="#tick"/></svg></div>
    <div class="cell c5" style="grid-row:5"><svg class="tick"><use href="#tick"/></svg></div>
    <div class="cell c5" style="grid-row:6"><svg class="tick"><use href="#tick"/></svg></div>
    <div class="cell c5" style="grid-row:7"><svg class="tick"><use href="#tick"/></svg></div>
    <div class="cell c5" style="grid-row:8"><svg class="tick"><use href="#tick"/></svg></div>
    <div class="cell c5" style="grid-row:9"><svg class="tick"><use href="#tick"/></svg></div>
    <div class="cell c5" style="grid-row:10"><svg class="tick"><use href="#tick"/></svg></div>
    <div class="cell c5" style="grid-row:11"><svg class="tick"><use href="#tick"/></svg></div>
    <div class="cell c5" style="grid-row:12"><svg class="tick"><use href="#tick"/></svg></div>
    <div class="cell c5" style="grid-row:13"><svg class="tick"><use href="#tick"/></svg></div>
    <div class="cell c5" style="grid-row:14"><svg class="tick"><use href="#tick"/></svg></div>

    <div class="cell c6" style="grid-row:2"><svg class="tick"><use href="#tick"/></svg></div>
    <div class="cell c6" style="grid-row:3"><svg class="tick"><use href="#tick"/></svg></div>
    <div class="cell c6" style="grid-row:4"><svg class="tick"><use href="#tick"/></svg></div>
    <div class="cell c6" style="grid-row:5"><svg class="tick"><use href="#tick"/></svg></div>
    <div class="cell c6" style="grid-row:6"><svg class="tick"><use href="#tick"/></svg></div>
    <div class="cell c6" style="grid-row:7"><svg class="tick"><use href="#tick"/></svg></div>
    <div class="cell c6" style="grid-row:8"><svg class="tick"><use href="#tick"/></svg></div>
    <div class="cell c6" style="grid-row:9"><svg class="tick"><use href="#tick"/></svg></div>
    <div class="cell c6" style="grid-row:10"><svg class="tick"><use href="#tick"/></svg></div>
    <div class="cell c6" style="grid-row:11"><svg class="tick"><use href="#tick"/></svg></div>
    <div class="cell c6" style="grid-row:12"><svg class="tick"><use href="#tick"/></svg></div>
    <div class="cell c6" style="grid-row:13"><svg class="tick"><use href="#tick"/></svg></div>
    <div class="cell c6" style="grid-row:14"><svg class="tick"><use href="#tick"/></svg></div>
    <div class="cell c6" style="grid-row:15"><svg class="tick"><use href="#tick"/></svg></div>
    <div class="cell c6" style="grid-row:16"><svg class="tick"><use href="#tick"/></svg></div>
  </section>

  <footer class="contact">
    <span><span class="label">Email</span>enquiries@brantwellpartners.gg</span>
    <span><span class="label">Telephone</span>01481 439216</span>
  </footer>
</main>
</body>
</html>
```